Electrical company needs a brochure designed for electrical construction work

we need a brochure designed for our company BRONZEPATH ELECTRICAL INSTALLATIONS. we are a group of electricians working in the construction industry delivering electrical constructon services to builders and other clients in the commercial and Industrial working environments. we would like our logo to stand out with a dark theme and also give a professional fee.l we have a brief description of what we do and our experiences in a word doc i will provide it along with our logo design

Target Market(s)

builders for commercial and industrial construction projects

Industry/Entity Type

Electric Company

Font styles to use
Serif

Colors
0456a4
96b7d9
5c5c5c
757575
000000
aaaaaa
ec1f27
33a6d7
0493ce

Requirements
Must have
• a professional feel,
Nice to have
• some wording that makes us stand out and brings all the attention

```html
<!DOCTYPE html>
<html lang="en">
<head>
<meta charset="utf-8">
<title>Bronzepath Electrical Installations – Brochure</title>
<link href="https://fonts.googleapis.com/css2?family=Roboto:wght@300;400;500;700;900&family=Roboto+Condensed:wght@400;700&display=swap" rel="stylesheet">
<style>
:root{
  --backdrop:#8a8a8a;
  --paper:#f4f4f4;
  --dark:#2a2a2c;
  --red:#ec1f27;
  --blue:#33a6d7;
  --blue-deep:#0493ce;
  --ink:#333;
  --grey:#5c5c5c;
  --white:#fff;
}
*{box-sizing:border-box;margin:0;padding:0}
html,body{width:847px;height:1200px;overflow:hidden}
body{background:radial-gradient(ellipse at 50% 45%,#b5b5b5 0%,var(--backdrop) 100%);font-family:"Roboto",sans-serif;position:relative;color:var(--ink)}
.spread{position:absolute;left:56px;width:736px;height:522px;background:var(--paper);box-shadow:0 14px 26px rgba(0,0,0,.45);overflow:hidden}
.spread--outer{top:55px}
.spread--inner{top:622px}
.edge{position:absolute;left:0;width:100%;height:5px;display:flex}
.edge span{height:100%}
.edge--top{top:0}
.edge--bottom{bottom:0}
.photo{position:absolute}
.copy{position:absolute;font-size:5.6px;line-height:1.38;text-align:justify;color:var(--ink)}
.copy p+p{margin-top:8px}
/* outer spread */
.cover-panel{position:absolute;left:368px;top:0;width:368px;height:522px;background:linear-gradient(160deg,#333336,#1f1f21)}
.brand{position:absolute;display:flex;align-items:center;gap:6px;color:var(--blue);font-weight:700;white-space:nowrap}
.brand .dot{border-radius:50%;background:var(--blue)}
.brand__text{display:flex;flex-direction:column;line-height:1}
.brand--cover{left:442px;top:30px}
.brand--cover .dot{width:24px;height:24px}
.brand--cover .name{font-size:28px;letter-spacing:.5px}
.brand--cover .sub{font-size:8.4px;letter-spacing:1px;margin-top:3px}
.brand--small{left:236px;top:442px}
.brand--small .dot{width:12px;height:12px}
.brand--small .name{font-size:12.5px}
.brand--small .sub{font-size:4px;letter-spacing:.4px;margin-top:1px}
.accent-bar{position:absolute;height:4px;background:var(--red)}
.contact{position:absolute;left:38px;top:374px}
.contact h2{font-size:12.5px;font-weight:500;color:var(--red);letter-spacing:.2px}
.contact .rule{width:20px;height:2px;background:var(--blue);margin:5px 0 12px}
.contact li{list-style:none;display:flex;gap:7px;font-size:10px;font-weight:300;color:var(--grey);margin-bottom:6px;line-height:1.2}
.contact svg{flex:none;margin-top:2px}
.headline{position:absolute;left:368px;width:368px;top:434px;text-align:center}
.headline h1{font-family:"Roboto Condensed",sans-serif;font-weight:700;font-size:25px;color:var(--blue);letter-spacing:.3px}
.headline p{font-size:12.4px;font-weight:300;color:var(--white);margin-top:2px}
.footer-bar{position:absolute;left:0;bottom:0;width:736px;height:34px}
.footer-bar svg{position:absolute;inset:0}
.footer-text{position:absolute;color:var(--white);font-size:11.5px;top:9px;display:flex;align-items:center;gap:5px}
.footer-text--web{left:38px;font-weight:400}
.footer-text--call{left:405px;font-weight:700;letter-spacing:.3px}
.footer-text--abn{left:605px;font-weight:700;font-size:11px}
.social{position:absolute;left:273px;top:10px;display:flex;gap:6px}
.social span{width:13px;height:13px;border-radius:50%;background:var(--blue-deep);border:1px solid rgba(255,255,255,.5)}
/* inner spread */
.intro-box{position:absolute;left:0;top:156px;width:368px;height:104px;background:var(--red);color:var(--white);padding:11px 28px 0 31px;font-size:7px;line-height:1.32;text-align:justify}
.jobs{position:absolute;left:33px;top:281px;list-style:none}
.jobs li{display:flex;gap:6px;font-size:7.3px;font-weight:700;color:#222;margin-bottom:5px;line-height:1.2;width:235px}
.jobs svg{flex:none;margin-top:0}
</style>
</head>
<body>

<!-- outer spread: back + cover -->
<section class="spread spread--outer">
  <div class="edge edge--top"><span style="width:40%;background:var(--red)"></span><span style="width:8%;background:var(--paper)"></span><span style="width:33%;background:var(--blue)"></span><span style="width:19%;background:var(--red)"></span></div>

  <div class="cover-panel"></div>

  <div class="copy" style="left:31px;top:36px;width:193px">
    <p>Electrical contracting company able to perform a great variety of electrical work required, recent experience on heavy industrial electrical installs involving complex systems on gas plant, 5 years total. Commercial and industrial situations are something we have always been exposed to and have been involved in many large construction jobs around Darwin.</p>
    <p>We are a small company just getting started and have been operating part time for over a year working late nights after our day jobs, working most weekends Saturday and Sundays, working towards building our company to be able to work full time and grow our business to something we can be proud of.</p>
  </div>

  <div class="photo" role="img" aria-label="Electrician in hard hat working on a switchboard" style="left:31px;top:165px;width:146px;height:166px;background:linear-gradient(135deg,#d9d4cc,#8d7a66 55%,#5b5650)"></div>
  <div class="photo" role="img" aria-label="Open switchboard with wiring" style="left:191px;top:165px;width:60px;height:166px;background:linear-gradient(160deg,#cfcfcf,#5e6166 60%,#2f3236)"></div>
  <div class="photo" role="img" aria-label="Gloved hands testing circuit breakers with a multimeter" style="left:243px;top:97px;width:493px;height:302px;background:linear-gradient(110deg,#bdbab3 0%,#6b5d4c 30%,#d7c38a 60%,#c9c9c9 100%)"></div>

  <div class="accent-bar" style="left:395px;top:93px;width:113px"></div>
  <div class="accent-bar" style="left:520px;top:398px;width:140px"></div>

  <div class="brand brand--cover"><span class="dot"></span><span class="brand__text"><span class="name">BRONZEPATH</span><span class="sub">ELECTRICAL INSTALLATIONS</span></span></div>

  <div class="contact">
    <h2>CONTACT DETAILS</h2>
    <div class="rule"></div>
    <ul>
      <li><svg width="7" height="9" viewBox="0 0 7 9"><path d="M3.5 0A3 3 0 0 0 .5 3c0 2.2 3 6 3 6s3-3.8 3-6a3 3 0 0 0-3-3zm0 4.2a1.2 1.2 0 1 1 0-2.4 1.2 1.2 0 0 1 0 2.4z" fill="#ec1f27"/></svg><span>Address line 1<br>Address line 2, Address line 2</span></li>
      <li><svg width="8" height="8" viewBox="0 0 8 8"><circle cx="4" cy="4" r="3.4" fill="none" stroke="#ec1f27" stroke-width=".9"/><path d="M2.8 2.3l.8-.2.5 1.1-.5.4c.2.5.6.9 1 1.1l.4-.5 1.1.5-.2.8c-1.6.2-3.3-1.6-3.1-3.2z" fill="#ec1f27"/></svg><span>0400555019</span></li>
      <li><svg width="8" height="7" viewBox="0 0 8 7"><rect x=".4" y=".9" width="7.2" height="5.2" fill="none" stroke="#ec1f27" stroke-width=".8"/><path d="M.4 1l3.6 2.8L7.6 1" fill="none" stroke="#ec1f27" stroke-width=".8"/></svg><span>bronzepath@example.com.au</span></li>
    </ul>
  </div>

  <div class="brand brand--small"><span class="dot"></span><span class="brand__text"><span class="name">BRONZEPATH</span><span class="sub">ELECTRICAL INSTALLATIONS</span></span></div>

  <div class="headline">
    <h1>WE ARE THE BEST</h1>
    <p>Electrical contracting company near you</p>
  </div>

  <div class="footer-bar">
    <svg width="736" height="34" viewBox="0 0 736 34"><polygon points="0,0 240,0 255,34 0,34" fill="#ec1f27"/><polygon points="240,0 578,0 563,34 255,34" fill="#0493ce"/><polygon points="578,0 736,0 736,34 563,34" fill="#ec1f27"/><polygon points="572,0 580,0 565,34 557,34" fill="#fff"/><polygon points="238,0 246,0 261,34 253,34" fill="#fff"/></svg>
    <div class="footer-text footer-text--web"><svg width="11" height="11" viewBox="0 0 11 11"><circle cx="5.5" cy="5.5" r="4.8" fill="none" stroke="#fff"/><ellipse cx="5.5" cy="5.5" rx="2" ry="4.8" fill="none" stroke="#fff" stroke-width=".8"/><path d="M.7 5.5h9.6" stroke="#fff" stroke-width=".8"/></svg>www.bronzepathelectrical.com.au</div>
    <div class="social"><span></span><span></span><span></span></div>
    <div class="footer-text footer-text--call">CALL NOW - 0400555019</div>
    <div class="footer-text footer-text--abn">ABN: 00 0000 000 00</div>
  </div>
</section>

<!-- inner spread -->
<section class="spread spread--inner">
  <div class="photo" role="img" aria-label="Rows of terminal blocks with black and yellow wiring" style="left:0;top:0;width:368px;height:156px;background:linear-gradient(180deg,#3b3d40 0%,#d8d3c6 45%,#b9a46a 80%,#3a3a3a 100%)"></div>

  <div class="intro-box">I'm Dale Mercer a local electrician in Darwin running a small electrical contracting company Bronzepath Electrical Installations. If you are in need of reliable, punctual, and experienced electricians to work in with your company then please give me a call I'm happy to discuss my business or submit a quote for any work you may have available. I have a lot of experience in the local construction industry I have worked on a lot of commercial and industrial construction jobs around Darwin for at least the last 10 years some jobs include.</div>

  <div class="copy" style="left:400px;top:37px;width:305px">
    <p>This list is not every job I have worked on but it gives a clear picture of what work I can perform as an electrical contractor. Most of the listed jobs I worked in a leadership role as either a leading hand or supervisor so I have been involved in construction meetings and meeting deadlines and working in with other contractors to achieve the best results for all parties involved. I'm trying to keep it short and sweet but if you decide to go with Bronzepath electrical installations to do your electrical work you will not regret it. I pride myself on my quality of work, work ethics and my prices are competitive.</p>
    <p style="margin-top:24px">Recently the opportunity arose that we could move away from our employment and take the business to a new level and work full time with 100% commitment we believe that our drive and passion for our trade and industry separates us from the unwilling and we will push ourselves to the limit to achieve and exceed any expectations that are placed upon us.</p>
    <p>Our background in large commercial and industrial construction jobs around Darwin has granted us the ability to introduce and implement stringent safety practices, we will always encourage and drive safety to the best of our ability to mitigate risk or harm to any person, not just because of our duty of care but because we like to see potential work colleagues/employees go home safely to their families unharmed.</p>
  </div>

  <div class="photo" role="img" aria-label="Hands holding a multimeter and probes testing a breaker panel" style="left:279px;top:215px;width:457px;height:290px;background:linear-gradient(120deg,#3e4145 0%,#c9c6bf 35%,#7f8a9a 55%,#d99a4a 75%,#6a6f75 100%)"></div>

  <ul class="jobs">
    <li><svg width="8" height="8" viewBox="0 0 8 8"><path d="M1 4.2l2 2L7 1.6" fill="none" stroke="#33a6d7" stroke-width="1.2"/></svg>Northgate high school</li>
    <li><svg width="8" height="8" viewBox="0 0 8 8"><path d="M1 4.2l2 2L7 1.6" fill="none" stroke="#33a6d7" stroke-width="1.2"/></svg>St Albury college</li>
    <li><svg width="8" height="8" viewBox="0 0 8 8"><path d="M1 4.2l2 2L7 1.6" fill="none" stroke="#33a6d7" stroke-width="1.2"/></svg>Underground cabling on many subdivisions including Ridgeview, Oakmere, Lowfield</li>
    <li><svg width="8" height="8" viewBox="0 0 8 8"><path d="M1 4.2l2 2L7 1.6" fill="none" stroke="#33a6d7" stroke-width="1.2"/></svg>Deskline stores</li>
    <li><svg width="8" height="8" viewBox="0 0 8 8"><path d="M1 4.2l2 2L7 1.6" fill="none" stroke="#33a6d7" stroke-width="1.2"/></svg>Eastlake substation HV switch gear</li>
    <li><svg width="8" height="8" viewBox="0 0 8 8"><path d="M1 4.2l2 2L7 1.6" fill="none" stroke="#33a6d7" stroke-width="1.2"/></svg>Westbrook substation HV switch gear</li>
    <li><svg width="8" height="8" viewBox="0 0 8 8"><path d="M1 4.2l2 2L7 1.6" fill="none" stroke="#33a6d7" stroke-width="1.2"/></svg>The city waterfront wave pool etc</li>
    <li><svg width="8" height="8" viewBox="0 0 8 8"><path d="M1 4.2l2 2L7 1.6" fill="none" stroke="#33a6d7" stroke-width="1.2"/></svg>Harbour point receiving station project</li>
    <li><svg width="8" height="8" viewBox="0 0 8 8"><path d="M1 4.2l2 2L7 1.6" fill="none" stroke="#33a6d7" stroke-width="1.2"/></svg>Northern defence base single leap project</li>
    <li><svg width="8" height="8" viewBox="0 0 8 8"><path d="M1 4.2l2 2L7 1.6" fill="none" stroke="#33a6d7" stroke-width="1.2"/></svg>State government building multiple contracts</li>
    <li><svg width="8" height="8" viewBox="0 0 8 8"><path d="M1 4.2l2 2L7 1.6" fill="none" stroke="#33a6d7" stroke-width="1.2"/></svg>The city convention centre</li>
    <li><svg width="8" height="8" viewBox="0 0 8 8"><path d="M1 4.2l2 2L7 1.6" fill="none" stroke="#33a6d7" stroke-width="1.2"/></svg>Air base runway lighting</li>
    <li><svg width="8" height="8" viewBox="0 0 8 8"><path d="M1 4.2l2 2L7 1.6" fill="none" stroke="#33a6d7" stroke-width="1.2"/></svg>Regional airport multiple different contracts</li>
    <li><svg width="8" height="8" viewBox="0 0 8 8"><path d="M1 4.2l2 2L7 1.6" fill="none" stroke="#33a6d7" stroke-width="1.2"/></svg>City hospital oncology building</li>
    <li><svg width="8" height="8" viewBox="0 0 8 8"><path d="M1 4.2l2 2L7 1.6" fill="none" stroke="#33a6d7" stroke-width="1.2"/></svg>City hospital multiple various maintenance contracts</li>
    <li><svg width="8" height="8" viewBox="0 0 8 8"><path d="M1 4.2l2 2L7 1.6" fill="none" stroke="#33a6d7" stroke-width="1.2"/></svg>Regional correctional facility</li>
  </ul>

  <div class="edge edge--bottom"><span style="width:40%;background:var(--red)"></span><span style="width:8%;background:var(--paper)"></span><span style="width:33%;background:var(--blue)"></span><span style="width:19%;background:var(--red)"></span></div>
</section>

</body>
</html>
```